Brava Set CEO and Partners Business Card

We need a fresh, fun, simple and clean business card design....we would like a template where we can add a name and title (as well as specific email addresses). We are open to different looks (full logo on one side and a small logo on the company info side, or our logo is in the background but faint on one side but full on the other, or something else cool :-) ). Our colors are in our logo: blue, black and white...however we are not opposed to the use of other colors if it works. We build sets, make props and a host of other things for the film and television industry...our card should reflect creativity, style and professionalism.

A white background would be preferred.

I would like to see an option with Facebook and Instagram icons.

Facebook- facebook.com/bravasetny
Instagram- brava_set

Our website is bravaset-example.com.

Brava Set, Inc.
418 Corvell Avenue, Unit 9
North Hollywood, California 91602
555.210.4873 | tel
555.210.6692 | fax
www.BravaSet-example.com

Sample Name and Title #1:

Peter Halvik
CEO / Co-Owner
555.210.4873 | tel
555.210.6692 | fax
peter@bravaset-example.com
www.BravaSet-example.com

Target Market(s)

Marketing Professionals, Production Designers, Interior Designers, Film Producers, Directors, Art Directors, Event Directors

Industry/Entity Type

Entertainment Industry

Contact Information for Business Card

Peter Halvik
CEO / Co-Owner
555.210.4873 | tel
555.210.6692 | fax
peter@bravaset-example.com
www.BravaSet-example.com

Font styles to use
Sans Serif

Colors
33a6d7
ffffff
1b1b1b

Requirements
Must have
• Logo, All Contact Info, White Background. Symmetry.
Nice to have
• Facebook and Instagram icons with addresses
• Facebook- facebook.com/bravasetny
• Instagram- brava_set

```html
<!DOCTYPE html>
<html lang="en">
<head>
<meta charset="utf-8">
<title>Brava Set — Business Card</title>
<link href="https://fonts.googleapis.com/css2?family=Open+Sans:wght@400;700;800&display=swap" rel="stylesheet">
<style>
  :root {
    --blue: #33a6d7;
    --white: #ffffff;
    --black: #1b1b1b;
    --backdrop: #8d8d8d;
  }
  * { margin: 0; padding: 0; box-sizing: border-box; }
  html, body { width: 1200px; height: 1074px; overflow: hidden; }
  body {
    background: var(--backdrop);
    font-family: "Open Sans", sans-serif;
    position: relative;
  }
  .card {
    position: absolute;
    left: 220px;
    width: 760px;
    height: 434px;
    background: var(--black);
    overflow: hidden;
  }
  .card--front { top: 70px; }
  .card--back { top: 570px; }

  /* front */
  .front-white { position: absolute; left: 24px; top: 40px; width: 190px; height: 86px; background: var(--white); }
  .front-blue { position: absolute; left: 24px; top: 126px; width: 190px; height: 264px; background: var(--blue); }
  .front-logo {
    position: absolute; left: 300px; top: 170px;
    font-weight: 800; font-size: 68px; letter-spacing: 1px;
    color: var(--white); text-transform: uppercase; line-height: 1;
  }

  /* back */
  .back-white { position: absolute; left: 190px; top: 40px; right: 0; height: 116px; background: var(--white); }
  .back-blue { position: absolute; left: 190px; top: 156px; right: 0; height: 234px; background: var(--blue); }
  .back-logo {
    position: absolute; left: 212px; top: 58px;
    font-weight: 800; font-size: 56px; color: var(--black);
    text-transform: uppercase; line-height: 1;
  }
  .person { position: absolute; left: 212px; top: 128px; color: var(--black); }
  .person-name { font-weight: 800; font-size: 23px; line-height: 1.15; }
  .person-title { font-size: 15px; line-height: 1.4; }
  .contact-list { position: absolute; left: 212px; top: 196px; list-style: none; color: var(--black); font-size: 15px; }
  .contact-list li { display: flex; align-items: flex-start; gap: 10px; line-height: 1.35; margin-bottom: 4px; }
  .contact-list svg { flex: none; width: 14px; height: 14px; margin-top: 3px; fill: var(--white); }
  .social { position: absolute; left: 570px; top: 170px; list-style: none; color: var(--black); font-size: 15px; }
  .social li { display: flex; align-items: center; gap: 9px; margin-bottom: 8px; }
  .social .mark { width: 13px; height: 13px; background: var(--white); }
</style>
</head>
<body>
  <section class="card card--front" aria-label="Card front">
    <div class="front-white"></div>
    <div class="front-blue"></div>
    <div class="front-logo">Brava Set</div>
  </section>

  <section class="card card--back" aria-label="Card back">
    <div class="back-white"></div>
    <div class="back-blue"></div>
    <div class="back-logo">Brava Set</div>
    <div class="person">
      <div class="person-name">Peter Halvik</div>
      <div class="person-title">CEO / Co-Owner</div>
    </div>
    <ul class="contact-list">
      <li><svg viewBox="0 0 16 16"><path d="M3 1h3l1 4-2 1a9 9 0 0 0 5 5l1-2 4 1v3a2 2 0 0 1-2 2A13 13 0 0 1 1 3a2 2 0 0 1 2-2z"/></svg>555.210.4873</li>
      <li><svg viewBox="0 0 16 16"><path d="M4 1h6v4H4zM2 6h12v9H2zm3 3v2h2V9zm4 0v2h2V9z"/></svg>555.210.6692</li>
      <li><svg viewBox="0 0 16 16"><path d="M1 3h14v2L8 9 1 5zm0 4 7 4 7-4v6H1z"/></svg>peter@bravaset-example.com</li>
      <li><svg viewBox="0 0 16 16"><path d="M8 1a7 7 0 1 0 0 14A7 7 0 0 0 8 1zm0 1.5c.8 1 1.4 2.6 1.5 4.5h-3C6.6 5.1 7.2 3.5 8 2.5zM2.6 7h2.4c.1-1.6.5-3 1.1-4A5.5 5.5 0 0 0 2.6 7zm8.4 0h2.4A5.5 5.5 0 0 0 9.9 3c.6 1 1 2.4 1.1 4zM2.6 9a5.5 5.5 0 0 0 3.5 4c-.6-1-1-2.4-1.1-4zm3.9 0c.1 1.9.7 3.5 1.5 4.5.8-1 1.4-2.6 1.5-4.5zm4.5 0c-.1 1.6-.5 3-1.1 4a5.5 5.5 0 0 0 3.5-4z"/></svg>www.BravaSet-example.com</li>
      <li><svg viewBox="0 0 16 16"><path d="M8 1a5 5 0 0 0-5 5c0 4 5 9 5 9s5-5 5-9a5 5 0 0 0-5-5zm0 3a2 2 0 1 1 0 4 2 2 0 0 1 0-4z"/></svg><span>418 Corvell Avenue, Unit 9<br>North Hollywood, California 91602</span></li>
    </ul>
    <ul class="social">
      <li><span class="mark"></span>bravasetny</li>
      <li><span class="mark"></span>brava_set</li>
    </ul>
  </section>
</body>
</html>
```